Design a Crossfit Flyer to attract new membership

With constantly updating workouts and the nutritional help Tollmere Ironworks is more than just an average gym. It’s a place for everyone to get healthy in a stress-free, safe and friendly environment.

Target Market(s)

Women ages 25-60 years old

Industry/Entity Type

Environment

Font styles to use
Serif

Requirements
Must have
• Please read thru the following info before you begin your design:
• Crossfit Flyer Information
• Please keep in mind a few things:
• 1) Our facility colors orange and green (you can see from my website what the color scheme is)
• 2) Our target demo graphic is women between the ages of 25-60, a large majority of my current clientele are middle aged women 45-60 years old
• 3) Try to keep it clean, and white (like quills website) if possible
• Side 1: (image of equipment and a younger women working out)
• 1) TMIW Logo
• 2) FREE WEEK TRIAL (big font) Sing up at www.tmironworks.net/schedulesign-up
• 3) Schedule: Monday-Friday 5:30am – 6:15am – 6:00pm – 7:00pm
• 4) Rates: $150/ Month Unlimited Classes - $100 /10 session package
• *15% discount for all fire, police, military, veterans, teachers, current students & trade association members
• 5) Address: 217 Pell Avenue Staten Island, NY 10308
• 6) Contact info: Phone: 347-518-7064 Email: tmironworks@mailbox.example
• 7) Website and Social media www.tmironworks.net find us @TMIronworks on Pagewall, Chirpline, Snapgrid, Reviewly, Circleplus and spotcheck
• Side 2 (image of a women working out, preferable middle aged):
• 1) 6 Benefits of CrossFit:
• a. Benefit #1: It BLASTS calories
• b. Benefit #2: It’s great Cardiovascular conditioning
• c. Benefit #3: It increases joint mobility
• d. Benefit #4: Everyday is something different, guaranteed
• e. Benefit #5: You’ll make new friends
• f. Benefit #6: You’ll feel like a badass
• 2) Free Week Trial Class (smaller font at the bottom) sign up at: www.tmironworks.net/schedulesign-up

```html
<!DOCTYPE html>
<html lang="en">
<head>
<meta charset="utf-8">
<title>Tollmere Ironworks – Free Week Trial Flyer</title>
<link href="https://fonts.googleapis.com/css2?family=Bebas+Neue&family=Arimo:wght@700&display=swap" rel="stylesheet">
<style>
  :root {
    --page: #ffffff;
    --orange-light: #f5a43a;
    --orange: #e98a1f;
    --orange-deep: #c9650f;
    --photo-warm: #e8924a;
    --photo-shade: #d27a30;
    --ink: #2b2b2b;
    --white: #ffffff;
    --rule: #3a2a1a;
    --green: #3dbb4f;
    --green-deep: #2fa84a;
    --blue: #2c3f9c;
  }
  * { margin: 0; padding: 0; box-sizing: border-box; }
  html, body { width: 1200px; height: 1000px; overflow: hidden; background: var(--page); }
  .canvas { position: relative; width: 1200px; height: 1000px; }
  .flyer {
    position: absolute; left: 159px; top: 149px; width: 884px; height: 684px; overflow: hidden;
    background: radial-gradient(ellipse at 45% 40%, var(--orange-light) 0%, var(--orange) 55%, var(--orange-deep) 100%);
    font-family: "Bebas Neue", "Oswald", sans-serif;
    color: var(--ink);
  }
  .athlete-photo {
    position: absolute; left: 600px; top: 0; width: 284px; height: 596px;
    background: linear-gradient(90deg, rgba(232,146,74,0) 0%, var(--photo-warm) 35%, var(--photo-shade) 100%);
  }
  .headline {
    position: absolute; left: 29px; top: 22px; font-size: 148px; line-height: 1;
    letter-spacing: -3px; color: var(--ink); white-space: nowrap;
    transform: scaleX(0.9); transform-origin: left top;
  }
  .signup {
    position: absolute; left: 191px; top: 146px; font-family: "Arimo", Arial, sans-serif;
    font-weight: 700; font-size: 21px; color: var(--ink); white-space: nowrap;
  }
  .signup .url { color: var(--white); }
  .info-block { position: absolute; left: 0; }
  .info-label { padding-left: 32px; font-size: 19px; line-height: 1; border-bottom: 1.5px solid var(--rule); padding-bottom: 3px; }
  .info-value { padding-left: 32px; font-size: 26px; line-height: 1; color: var(--white); margin-top: 8px; white-space: nowrap; }
  .schedule { top: 208px; width: 482px; }
  .rates { top: 279px; width: 556px; }
  .contact { top: 350px; width: 600px; }
  .brand {
    position: absolute; left: 32px; top: 458px; width: 180px; display: flex; align-items: center; gap: 8px;
  }
  .brand-mark { width: 14px; height: 14px; background: var(--ink); flex: none; }
  .brand-name { font-size: 38px; line-height: 0.95; color: var(--ink); }
  .divider { position: absolute; left: 218px; top: 446px; width: 1.5px; height: 150px; background: var(--rule); }
  .discount {
    position: absolute; left: 249px; top: 456px; width: 392px; font-size: 23px; line-height: 27px;
    letter-spacing: 2px; color: var(--ink);
  }
  .footer-band {
    position: absolute; left: 0; top: 596px; width: 884px; height: 88px;
    background: linear-gradient(90deg, var(--green) 0%, var(--green-deep) 55%, var(--blue) 100%);
    padding: 22px 0 0 27px; font-family: "Arimo", Arial, sans-serif; font-weight: 700;
    font-size: 17.5px; line-height: 24px; color: var(--white); white-space: nowrap;
  }
</style>
</head>
<body>
<div class="canvas">
  <section class="flyer">
    <div class="athlete-photo" role="img" aria-label="Photo of a young woman in sportswear training with dumbbells"></div>

    <h1 class="headline">FREE WEEK TRIAL</h1>
    <p class="signup">Sign up at <span class="url">www.tmironworks.net/schedulesign-up</span></p>

    <div class="info-block schedule">
      <p class="info-label">Schedule [Monday-Friday]</p>
      <p class="info-value">5:30AM — 6:15AM / 6:00PM — 7:00PM</p>
    </div>
    <div class="info-block rates">
      <p class="info-label">Rates</p>
      <p class="info-value">$150/ Month Unlimited Classes - $100 /10 Session Package</p>
    </div>
    <div class="info-block contact">
      <p class="info-label">Contact Us</p>
      <p class="info-value">Phone: 347-518-7064 / Email: tmironworks@mailbox.example</p>
    </div>

    <div class="brand">
      <span class="brand-mark"></span>
      <span class="brand-name">Tollmere Ironworks</span>
    </div>
    <div class="divider"></div>
    <p class="discount">15% discount for all fire, police, military, veterans, teachers, current students &amp; trade association members</p>

    <footer class="footer-band">
      <p>Visit us at: www.tmironworks.net</p>
      <p>find us @TMIronworks on Pagewall, Chirpline, Snapgrid, Reviewly, Circleplus and spotcheck</p>
    </footer>
  </section>
</div>
</body>
</html>
```